What does your organisation do?
TALVO
We need a website for our business – A Holding Company

Objective:
1. User-friendly design and navigation
2. Content management
3. Language (English and Arabic)
4. Download PDF or scan for profile

Navigations and Sub-Navigations:
1. Profile
a. About Us
b. Vision-Mission
c. Corporate Governance
d. Sustainability
2. Business Sector
a. Food
b. Logistics
c. Retail
d. Trading and Distribution
e. Government Services
3. Investor Relations
4. Careers
5. Contact Us
Footer:
Contact Us
1. Address
2. Contact Number
3. Email Address
4. Social Media (LinkedIn Logo)
Company / Quick Links
• About Us
• Vision & Mission
• Careers

Newsletter
Get the latest information from us and our group companies. Be amongst the first to know and stay updated on the go. Join our mailing list
Email Text Box with Subscribe button.

Competitors / Reference:
URL 1: https://www.quirenholding.example/
URL 2: https://www.mibelholding.example/
URL 3: https://vzp.example

Target Market(s)

Individual and customer businesses customers

Industry/Entity Type

Financial

Coding

Coded - Design and coding required

Number of Pages Required

5+ page

Font styles to use
Serif
Sans Serif

Requirements
Must have

• 1. SEO Friendly website ( Meta tags, description, title, proper keywords)
2. Ability to make modifications easily in future. (Provide front end for adding content, images etc.)
3. Chatbot Widget with enquiry form – integration with google sheet
4. Register website with Google (Google Search Console)
5. Register website with Google My Business
Nice to have
• See uploaded file for reference

```html
<!DOCTYPE html>
<html lang="en">
<head>
<meta charset="utf-8">
<title>TALVO Holding – Diversified Investments</title>
<meta name="description" content="TALVO is a diversified holding company with businesses in food, logistics, retail, trading and distribution, and government services.">
<link href="https://fonts.googleapis.com/css2?family=Titillium+Web:wght@300;400;600&family=Roboto:wght@300;400&family=Noto+Kufi+Arabic:wght@400&display=swap" rel="stylesheet">
<style>
:root{
  --accent:#2cc3f2;
  --navy:#1a3551;
  --footer:#1d3a5b;
  --footer-line:#2a4a6e;
  --ink:#2c2c2c;
  --muted:#6f6f6f;
  --card:#f6f7f9;
  --white:#ffffff;
}
*{margin:0;padding:0;box-sizing:border-box}
html,body{width:1200px;height:2498px;overflow:hidden;background:var(--white)}
body{font-family:"Roboto",sans-serif;color:var(--ink);position:relative}
a{text-decoration:none;color:inherit}

/* header */
.site-header{position:absolute;left:0;top:0;width:1200px;height:84px}
.brand{position:absolute;left:60px;top:16px;font-family:"Titillium Web",sans-serif;font-weight:600;font-size:40px;line-height:48px;color:var(--accent);letter-spacing:.5px}
.main-nav{position:absolute;left:297px;top:31px;display:flex;gap:30px;font-family:"Titillium Web",sans-serif;font-size:14px;line-height:20px;color:#777;letter-spacing:.5px;white-space:nowrap}
.main-nav .active{color:var(--accent)}
.header-tools{position:absolute;right:60px;top:30px;display:flex;align-items:center;gap:10px;font-family:"Titillium Web",sans-serif;font-size:14px;line-height:20px;color:#777;letter-spacing:.5px;white-space:nowrap}
.header-tools b{color:var(--accent);font-weight:400;font-size:15px}
.lang-switch{margin-left:8px;padding-left:12px;border-left:1px solid #ddd;font-family:"Noto Kufi Arabic",sans-serif;font-size:13px;color:var(--accent)}

/* hero */
.hero{position:absolute;left:0;top:84px;width:1200px;height:583px;
  background:linear-gradient(100deg,#c9cbc8 0%,#b89a78 28%,#d8a56a 48%,#8c6a55 65%,#c98a4e 85%,#f0b25c 100%)}
.hero-panel{position:absolute;left:751px;top:50px;width:389px;height:383px;background:rgba(44,116,144,.82);padding:48px 55px 0 40px;text-align:right;color:var(--white)}
.hero-panel h1{font-family:"Titillium Web",sans-serif;font-weight:300;font-size:46px;line-height:54px;letter-spacing:.5px;white-space:nowrap}
.rule{display:block;width:42px;height:2px;background:var(--accent)}
.hero-panel .rule{margin:10px 0 30px auto}
.hero-panel p{font-size:12px;line-height:21px}
.btn{display:inline-block;font-family:"Titillium Web",sans-serif;font-weight:600;font-size:16px;letter-spacing:1px;border-radius:24px;text-align:center;white-space:nowrap}
.btn-solid{background:var(--accent);color:var(--white);width:190px;height:45px;line-height:45px;margin-top:20px}
.btn-outline{border:1px solid var(--accent);color:var(--accent);width:158px;height:45px;line-height:43px}

/* sector band */
.sector-band{position:absolute;left:0;top:667px;width:1200px;height:262px;background:var(--navy);display:flex;padding:48px 60px 0}
.sector{flex:1;text-align:center;color:#c9d3de;padding:0 10px}
.sector svg{display:block;margin:0 auto 6px}
.sector h3{font-family:"Titillium Web",sans-serif;font-weight:400;font-size:21px;line-height:28px;color:var(--white);margin-bottom:10px}
.sector.highlight h3{color:var(--accent)}
.sector p{font-size:12px;line-height:21px;font-weight:300}

/* sectors intro */
.special{position:absolute;left:60px;top:1005px;width:300px}
.section-title{font-family:"Titillium Web",sans-serif;font-weight:400;font-size:35px;line-height:44px;color:var(--ink);letter-spacing:.5px;white-space:nowrap}
.special .rule,.about-text .rule{margin:12px 0 26px}
.body-copy{font-size:12px;line-height:21px;color:var(--muted)}
.special .btn{margin-top:28px}
.card{position:absolute;top:1013px;width:337px;height:389px;background:var(--card);border:1px solid #eceef1}
.card-art{height:208px;background:#fff}
.card-art.gov{background:linear-gradient(120deg,#fff 20%,#e4e0f3 55%,#fff 90%)}
.card-art.investor{background:radial-gradient(circle at 50% 55%,#bcd9f1 0,#d9cdf2 35%,#fff 62%)}
.card-body{padding:20px 23px}
.card h4{font-family:"Titillium Web",sans-serif;font-weight:400;font-size:17px;line-height:24px;color:var(--ink);margin-bottom:10px}
.read-more{display:inline-flex;align-items:center;gap:4px;margin-top:16px;font-size:11px;color:var(--accent)}

/* banner */
.promo{position:absolute;left:0;top:1477px;width:1200px;height:225px;background:linear-gradient(90deg,#28b4e6 0%,#39bde9 55%,#1f9fd6 100%);color:var(--white)}
.promo-photo{position:absolute;left:790px;top:0;width:275px;height:225px;background:linear-gradient(180deg,#b9d9ea 0%,#e8d6cc 60%,#f3efec 100%)}
.promo-text{position:absolute;left:61px;top:30px;width:620px}
.promo-text h2{font-family:"Titillium Web",sans-serif;font-weight:400;font-size:34px;line-height:42px;margin-bottom:8px;white-space:nowrap}
.promo-text p{font-size:12px;line-height:21px}
.btn-white{background:var(--white);color:var(--ink);width:180px;height:45px;line-height:45px;margin-top:12px}

/* about */
.about-photo{position:absolute;left:60px;top:1778px;width:514px;height:360px;background:linear-gradient(135deg,#c9d4de 0%,#7d8fa3 40%,#b7c1cc 70%,#eef1f4 100%)}
.about-text{position:absolute;left:620px;top:1772px;width:480px}
.about-text .body-copy{margin-bottom:21px}

/* footer */
.site-footer{position:absolute;left:0;top:2212px;width:1200px;height:286px;background:var(--footer);color:#c2cddb}
.footer-col{position:absolute;top:40px}
.footer-col h5{font-family:"Titillium Web",sans-serif;font-weight:600;font-size:11.5px;color:var(--accent);letter-spacing:.3px;margin-bottom:14px}
.footer-brand{left:60px;top:38px;width:225px}
.footer-brand .brand{position:static;display:block;font-size:40px;line-height:44px;margin-bottom:6px}
.footer-brand p{font-size:12px;line-height:21px;color:var(--white)}
.link-list{list-style:none;font-family:"Titillium Web",sans-serif;font-size:12.5px;line-height:22.5px}
.link-list .active{color:var(--accent)}
.contact-row{display:flex;gap:14px;font-size:12px;line-height:21px;margin-bottom:16px}
.contact-row svg{flex:none;margin-top:4px}
.news-input{margin-top:16px;width:248px;height:37px;background:#eef1f4;display:flex;align-items:center;justify-content:space-between;padding:0 10px;font-size:11px;color:#9aa3ad}
.footer-bottom{position:absolute;left:0;top:220px;width:1200px;border-top:1px solid var(--footer-line)}
.copyright{position:absolute;left:61px;top:30px;font-size:11px;color:#c2cddb}
.copyright b{color:var(--accent);font-weight:400}
.social{position:absolute;right:60px;top:17px;display:flex;gap:8px}
.social span{width:34px;height:34px;border-radius:50%;background:#2b4d74;display:block}
</style>
</head>
<body>

<header class="site-header">
  <a class="brand" href="#">TALVO</a>
  <nav class="main-nav">
    <a class="active" href="#">Home</a><a href="#">Profile</a><a href="#">Business Sector</a><a href="#">Investor Relations</a><a href="#">Careers</a><a href="#">Contact Us</a>
  </nav>
  <div class="header-tools">
    <svg width="22" height="22" viewBox="0 0 24 24" fill="none" stroke="#2cc3f2" stroke-width="1.4"><path d="M5 3h4l2 5-3 2a12 12 0 0 0 6 6l2-3 5 2v4a2 2 0 0 1-2 2A18 18 0 0 1 3 5a2 2 0 0 1 2-2z"/></svg>
    CALL : <b>+971 4 000 0000</b>
    <a class="lang-switch" href="#" lang="ar">العربية</a>
  </div>
</header>

<section class="hero" role="img" aria-label="Photo of a cargo truck on a curved highway toward a city skyline at sunset">
  <div class="hero-panel">
    <h1>DIVERSIFIED<br>HOLDINGS</h1>
    <span class="rule"></span>
    <p>TALVO builds long-term value across food, logistics,<br>retail, trading and government services.</p>
    <a class="btn btn-solid" href="#">DOWNLOAD PROFILE</a>
  </div>
</section>

<section class="sector-band">
  <div class="sector">
    <svg width="60" height="40" viewBox="0 0 60 40" fill="none" stroke="#fff" stroke-width="1.6"><rect x="10" y="4" width="28" height="24"/><path d="M38 12h10l8 9v7H38z"/><circle cx="18" cy="32" r="4"/><circle cx="48" cy="32" r="4"/><path d="M2 12h6M0 18h8M4 24h4"/></svg>
    <h3>Logistics</h3>
    <p>Our logistics companies provide express shipping, warehousing and same-day delivery across the United Arab Emirates and the wider region.</p>
  </div>
  <div class="sector highlight">
    <svg width="60" height="40" viewBox="0 0 60 40" fill="none" stroke="#2cc3f2" stroke-width="1.6"><circle cx="28" cy="20" r="16"/><path d="M6 26c14 4 34-4 48-18M38 10l10-4-2 8z"/></svg>
    <h3>Trading and Distribution</h3>
    <p>A regional network of land, sea and air partners lets our trading arm source, import and distribute quality goods to businesses and customers.</p>
  </div>
  <div class="sector">
    <svg width="60" height="40" viewBox="0 0 60 40" fill="none" stroke="#fff" stroke-width="1.6"><rect x="14" y="8" width="16" height="18" transform="rotate(-20 22 17)"/><path d="M30 36l12-30h6"/><circle cx="28" cy="36" r="3"/></svg>
    <h3>Food &amp; Retail</h3>
    <p>From food production to retail stores, our brands serve families every day with trusted products, modern outlets and great customer service.</p>
  </div>
</section>

<section class="special">
  <h2 class="section-title">OUR SECTORS</h2>
  <span class="rule"></span>
  <p class="body-copy">TALVO is a holding company with a portfolio of businesses in five sectors: food, logistics, retail, trading and distribution, and government services. Each company is run by experienced teams and guided by strong corporate governance and a clear focus on sustainability.</p>
  <a class="btn btn-outline" href="#">VIEW ALL</a>
</section>

<article class="card" style="left:432px">
  <div class="card-art gov" role="img" aria-label="Illustration of a service officer beside a regional map"></div>
  <div class="card-body">
    <h4>GOVERNMENT SERVICES</h4>
    <p class="body-copy">Visa, licensing and PRO services that help companies get up and running quickly by removing time-consuming procedures.</p>
    <a class="read-more" href="#">read more <svg width="12" height="8" viewBox="0 0 12 8" fill="none" stroke="#2cc3f2"><path d="M0 4h11M8 1l3 3-3 3"/></svg></a>
  </div>
</article>

<article class="card" style="left:803px">
  <div class="card-art investor" role="img" aria-label="Illustration of a team around a globe with a growth chart and gears"></div>
  <div class="card-body">
    <h4>INVESTOR RELATIONS</h4>
    <p class="body-copy">Annual reports, financial results and governance updates for our shareholders and partners, all in one place.</p>
    <a class="read-more" href="#">read more <svg width="12" height="8" viewBox="0 0 12 8" fill="none" stroke="#2cc3f2"><path d="M0 4h11M8 1l3 3-3 3"/></svg></a>
  </div>
</article>

<section class="promo">
  <div class="promo-photo" role="img" aria-label="Photo of a customer support agent wearing a headset"></div>
  <div class="promo-text">
    <h2>Build your career with TALVO</h2>
    <p>Join a growing group of companies across five sectors. We look for people who bring energy, integrity and ideas, and we give them room to grow with us.</p>
    <a class="btn btn-white" href="#">VIEW CAREERS</a>
  </div>
</section>

<div class="about-photo" role="img" aria-label="Photo of a business team in discussion around a meeting table"></div>
<section class="about-text">
  <h2 class="section-title">ABOUT TALVO</h2>
  <span class="rule"></span>
  <p class="body-copy">TALVO is a UAE-based holding company that invests in and grows businesses serving individuals and companies. Our portfolio is agile, reliable and built for a fast changing world.</p>
  <p class="body-copy">Our vision is to be the region’s most trusted group of companies. Our mission is to create lasting value for customers, partners, employees and shareholders.</p>
  <p class="body-copy">Guided by sound corporate governance and a commitment to sustainability, we grow responsibly in every sector we serve.</p>
  <a class="btn btn-outline" href="#">LEARN MORE</a>
</section>

<footer class="site-footer">
  <div class="footer-col footer-brand">
    <a class="brand" href="#">TALVO</a>
    <p>A diversified holding company building value across food, logistics, retail, trading and government services.</p>
  </div>
  <div class="footer-col" style="left:339px">
    <h5>COMPANY</h5>
    <ul class="link-list">
      <li class="active">About Us</li><li>Vision &amp; Mission</li><li>Business Sector</li><li>Investor Relations</li><li>Careers</li>
    </ul>
  </div>
  <div class="footer-col" style="left:616px;width:240px">
    <h5>CONTACT US</h5>
    <div class="contact-row"><svg width="14" height="16" viewBox="0 0 14 16" fill="#2cc3f2"><path d="M7 0a6 6 0 0 1 6 6c0 4-6 10-6 10S1 10 1 6a6 6 0 0 1 6-6zm0 4a2 2 0 1 0 0 4 2 2 0 0 0 0-4z"/></svg><span>Office 1200, Example Tower, Business Bay, Dubai, UAE</span></div>
    <div class="contact-row"><svg width="14" height="14" viewBox="0 0 24 24" fill="#2cc3f2"><path d="M5 2h4l2 5-3 2a12 12 0 0 0 6 6l2-3 5 2v4a2 2 0 0 1-2 2A18 18 0 0 1 3 4a2 2 0 0 1 2-2z"/></svg><span>+971 4 000 0000</span></div>
    <div class="contact-row"><svg width="14" height="11" viewBox="0 0 14 11" fill="#2cc3f2"><path d="M0 0h14v2L7 6 0 2zM0 3.5l7 4 7-4V11H0z"/></svg><span>info@talvo.example</span></div>
  </div>
  <div class="footer-col" style="left:893px;width:250px">
    <h5>NEWSLETTER</h5>
    <p style="font-size:12px;line-height:21px">Get the latest news from us and our group companies. Join our mailing list.</p>
    <div class="news-input">Enter e-mail here... <svg width="16" height="10" viewBox="0 0 16 10" fill="none" stroke="#2cc3f2"><path d="M0 5h15M11 1l4 4-4 4"/></svg></div>
  </div>
  <div class="footer-bottom">
    <p class="copyright">© <b>TALVO</b> - 2020. All Rights Reserved.</p>
    <div class="social" aria-label="Social media links"><span></span><span></span><span></span><span></span></div>
  </div>
</footer>

</body>
</html>
```